Pregnancy and Fertility Information Website

Hello Designers,
I need a website which provide tips and information about healthy and happy pregnancy. My website name is Lorvin medical.

The website should provide all the information needed throughout pregnancy and beyond ranging from pregnancy tracking tools and articles about common pregnancy concerns and what to expect during pregnancy,etc.
The details about first trimester, second trimester and third trimester should be highlighted in the website.

Top Navigation
Home, Fertility, Pregnancy basics, Articles, Tips and News

I'm looking for a simple and clean design which involves captivating images and colors but it shouldn't be crowded. The design must be professional and modern. An easy to navigate layout is a must.

Green, violet, blue and light yellow colors are my favorites but i'm open to other options.

Any questions. Kindly ask

Industry/Entity Type

Medical

```html
<!DOCTYPE html>
<html lang="en">
<head>
<meta charset="utf-8">
<title>Lorvin medical – Pregnancy &amp; Fertility</title>
<link href="https://fonts.googleapis.com/css2?family=Open+Sans:wght@400;600;700&family=Roboto:wght@300;400&display=swap" rel="stylesheet">
<style>
  :root {
    --page-bg: #ffffff;
    --brand-green: #8bc34a;
    --brand-green-dark: #6ea33a;
    --brand-blue: #1f5fa8;
    --nav-active: #7cc04a;
    --icon-grey: #a9b1b8;
    --hero-top: #8f969c;
    --hero-mid: #a9a29b;
    --hero-low: #5d6168;
    --text-light: #ffffff;
    --dot-idle: rgba(255,255,255,0.55);
  }
  * { box-sizing: border-box; margin: 0; padding: 0; }
  html, body { width: 1200px; height: 663px; overflow: hidden; background: var(--page-bg); }
  body { font-family: "Open Sans", Arial, sans-serif; position: relative; }

  .site-header {
    position: absolute; left: 0; top: 0; width: 1200px; height: 59px;
    background: var(--page-bg);
  }
  .brand {
    position: absolute; left: 172px; top: 18px;
    display: flex; align-items: center; gap: 6px;
    font-family: "Open Sans", Arial, sans-serif; font-weight: 700;
    font-size: 15px; color: var(--brand-blue); letter-spacing: 0.2px;
  }
  .brand-dot { width: 12px; height: 12px; border-radius: 50%; background: var(--brand-green); }

  .main-nav { position: absolute; top: 0; left: 0; height: 59px; }
  .main-nav a {
    position: absolute; top: 24px; font-size: 9px; font-weight: 700;
    text-transform: uppercase; color: var(--brand-blue); text-decoration: none; letter-spacing: 0.2px;
    white-space: nowrap;
  }
  .main-nav a.is-active { color: var(--nav-active); font-weight: 600; }
  .main-nav a.is-active::before {
    content: ""; position: absolute; left: 0; right: 0; top: -24px; height: 3px; background: var(--nav-active);
  }
  .header-tools { position: absolute; top: 21px; left: 912px; height: 16px; }
  .header-tools svg { position: absolute; top: 0; }
  .tool-divider { position: absolute; left: 28px; top: 2px; width: 1px; height: 12px; background: #dde2e6; }
  .social-mark { position: absolute; top: 4px; width: 8px; height: 8px; border-radius: 50%; }

  .hero {
    position: absolute; left: 0; top: 59px; width: 1200px; height: 604px; overflow: hidden;
  }
  .hero-photo {
    position: absolute; inset: 0;
    background:
      radial-gradient(ellipse at 78% 55%, #cfc3b6 0%, rgba(207,195,182,0) 45%),
      radial-gradient(ellipse at 12% 30%, #4f5f4a 0%, rgba(79,95,74,0) 35%),
      radial-gradient(ellipse at 35% 70%, #3c4149 0%, rgba(60,65,73,0) 45%),
      linear-gradient(180deg, var(--hero-top) 0%, var(--hero-mid) 55%, var(--hero-low) 100%);
  }

  .hero-caption {
    position: absolute; left: 241px; top: 206px; width: 362px; height: 173px;
    background: var(--brand-green); color: var(--text-light);
    padding: 18px 24px 0 29px;
    clip-path: polygon(0 0, 317px 0, 362px 45px, 362px 173px, 0 173px);
  }
  .hero-fold { position: absolute; left: 558px; top: 206px; width: 45px; height: 45px; }
  .hero-title {
    font-family: "Roboto", Arial, sans-serif; font-weight: 300;
    font-size: 30px; line-height: 30px;
  }
  .hero-text { margin-top: 18px; font-size: 11px; line-height: 17px; }

  .hero-arrow { position: absolute; top: 334px; }
  .hero-arrow--prev { left: 62px; }
  .hero-arrow--next { left: 1114px; }

  .hero-dots { position: absolute; left: 561px; top: 611px - 59px; display: flex; gap: 9px; }
  .hero-dots span { width: 7px; height: 7px; border-radius: 50%; background: var(--dot-idle); }
  .hero-dots span.is-current { background: var(--brand-green); }
</style>
</head>
<body>
  <header class="site-header">
    <div class="brand"><span class="brand-dot"></span>Lorvin medical</div>
    <nav class="main-nav">
      <a href="#" class="is-active" style="left:510px">Home</a>
      <a href="#" style="left:560px">Fertility</a>
      <a href="#" style="left:625px">Pregnancy Basics</a>
      <a href="#" style="left:737px">Articles</a>
      <a href="#" style="left:803px">Tips and News</a>
    </nav>
    <div class="header-tools">
      <svg width="14" height="16" viewBox="0 0 14 16" aria-label="Search">
        <circle cx="6" cy="7" r="4.2" fill="none" stroke="var(--icon-grey)" stroke-width="1.5"/>
        <line x1="9" y1="10" x2="12.5" y2="13.5" stroke="var(--icon-grey)" stroke-width="1.6" stroke-linecap="round"/>
      </svg>
      <span class="tool-divider"></span>
      <span class="social-mark" style="left:40px;background:var(--brand-blue)"></span>
      <span class="social-mark" style="left:61px;background:var(--icon-grey)"></span>
      <svg style="left:80px" width="14" height="16" viewBox="0 0 14 16" aria-label="Email">
        <rect x="1" y="4" width="12" height="8" rx="1" fill="none" stroke="var(--icon-grey)" stroke-width="1.3"/>
        <polyline points="1.5,4.5 7,9 12.5,4.5" fill="none" stroke="var(--icon-grey)" stroke-width="1.3"/>
      </svg>
    </div>
  </header>

  <section class="hero">
    <div class="hero-photo" role="img" aria-label="Photo of an expectant couple smiling together on a sofa in a bright living room with a houseplant"></div>

    <div class="hero-caption">
      <h1 class="hero-title">Lorem ipsum dolor<br>sit amet dolor.</h1>
      <p class="hero-text">Lorem ipsum dolor sit amet, consectetur adipiscing elit.<br>Nam vestibulum nec ex feugiat congue.</p>
    </div>
    <svg class="hero-fold" viewBox="0 0 45 45" aria-hidden="true">
      <polygon points="0,0 45,45 0,45" fill="var(--brand-green-dark)"/>
    </svg>

    <svg class="hero-arrow hero-arrow--prev" width="20" height="36" viewBox="0 0 20 36" aria-label="Previous slide">
      <polyline points="16,4 4,18 16,32" fill="none" stroke="#ffffff" stroke-width="2"/>
    </svg>
    <svg class="hero-arrow hero-arrow--next" width="20" height="36" viewBox="0 0 20 36" aria-label="Next slide">
      <polyline points="4,4 16,18 4,32" fill="none" stroke="#ffffff" stroke-width="2"/>
    </svg>

    <div class="hero-dots" style="top:552px">
      <span class="is-current"></span><span></span><span></span><span></span><span></span>
    </div>
  </section>
</body>
</html>
```